Hi! We require a design for business cards for directors and head teachers of an international daycare for children 0 - 9. We are family-owned, -operated and -oriented. We have six locations, looking to franchise. Our USPs are: 1) Flexibility 2) Quality teachers 3) International culture 4) Best nutrition We are quality teachers and professional caretakers, but with creativity and personality! Business cards should be playful (but no Comic Sans or baby hand prints), colorful (but no rainbows), and have some breathing space. It should be obvious from the business card that we're a daycare. In 2020 we'll be launching our new website based on this design: https://plomvane.io/47K2RQLWZTD The font in the new website will be Houschka (medium, demibold, bold). We will keep our current logo, included in the files here. There are also screenshots of some designs we like. Show us your best! :)

Industry/Entity Type

Childcare

Contact Information for Business Card

Lotte de Vries-Bakhuis
Communications Wizard
Poppel Hoek International Daycare
Kastanjeweg 47 B, 2316 KR Leiden
www.poppelhoek.nl
+31 647315082

Font styles to use
Serif
Sans Serif

Colors

Designer to choose colors to be used in the design.

Requirements
Must have
• Color

```html
<!DOCTYPE html>
<html lang="en">
<head>
<meta charset="utf-8">
<title>Poppel Hoek – Business Card</title>
<link rel="stylesheet" href="https://fonts.googleapis.com/css2?family=Montserrat:wght@400;600;800&display=swap">
<style>
  :root {
    --pink: #e84c80;
    --blue: #1aa9dc;
    --paper: #faf8fb;
    --ink: #333338;
    --backdrop: #2b2b2d;
    --white: #ffffff;
  }
  * { box-sizing: border-box; margin: 0; padding: 0; }
  html, body {
    width: 1200px; height: 900px; overflow: hidden;
    background: var(--backdrop);
    font-family: "Montserrat", Arial, sans-serif;
  }
  .canvas {
    position: relative; width: 1200px; height: 900px;
    display: flex; flex-direction: column; align-items: center; justify-content: center; gap: 40px;
  }
  .card {
    position: relative; width: 700px; height: 400px; overflow: hidden;
    box-shadow: 0 14px 30px rgba(0,0,0,.45);
  }
  /* Front */
  .card--front { background: var(--pink); color: var(--white); }
  .front-mark {
    position: absolute; left: 0; right: 0; top: 140px;
    text-align: center; font-weight: 800; font-size: 64px; line-height: 1; letter-spacing: 1px;
    color: var(--white);
  }
  .front-tagline {
    position: absolute; left: 0; right: 0; top: 272px;
    text-align: center; font-size: 13px; font-weight: 400; letter-spacing: 2.6px; text-transform: uppercase;
  }
  /* Back */
  .card--back { background: var(--paper); }
  .back-mark {
    position: absolute; left: 0; right: 0; top: 78px;
    text-align: center; font-weight: 800; font-size: 50px; line-height: 1; color: var(--pink);
  }
  .person {
    position: absolute; right: 322px; top: 176px; text-align: right;
  }
  .person-name {
    font-weight: 800; font-size: 22px; line-height: 1.1; text-transform: uppercase; letter-spacing: -0.3px;
  }
  .person-name .first { color: var(--pink); }
  .person-name .last { color: var(--blue); }
  .person-role { font-size: 16px; color: var(--ink); margin-top: 4px; }
  .divider {
    position: absolute; left: 398px; top: 176px; width: 2px; height: 78px; background: var(--pink);
  }
  .contacts {
    position: absolute; left: 420px; top: 196px; list-style: none;
    font-size: 15px; color: var(--ink);
  }
  .contacts li { display: flex; align-items: center; gap: 12px; height: 26px; }
  .contacts svg { width: 16px; height: 16px; flex: none; }
  .address-band {
    position: absolute; left: 0; right: 0; top: 292px; height: 60px;
    background: var(--pink); color: var(--white);
    display: flex; align-items: center; justify-content: center;
    font-size: 15px; letter-spacing: 2.4px; text-transform: uppercase;
  }
</style>
</head>
<body>
<main class="canvas">
  <section class="card card--front">
    <div class="front-mark">POPPEL HOEK</div>
    <p class="front-tagline">Poppel Hoek International Daycare</p>
  </section>

  <section class="card card--back">
    <div class="back-mark">POPPEL HOEK</div>
    <div class="person">
      <h1 class="person-name"><span class="first">Lotte de </span><span class="last">Vries-Bakhuis</span></h1>
      <p class="person-role">Communications Wizard</p>
    </div>
    <div class="divider"></div>
    <ul class="contacts">
      <li>
        <svg viewBox="0 0 24 24" aria-hidden="true"><path fill="var(--pink)" d="M6.6 10.8a15.1 15.1 0 0 0 6.6 6.6l2.2-2.2c.3-.3.7-.4 1-.2 1.1.4 2.3.6 3.6.6.6 0 1 .4 1 1V20c0 .6-.4 1-1 1A17 17 0 0 1 3 4c0-.6.4-1 1-1h3.5c.6 0 1 .4 1 1 0 1.3.2 2.5.6 3.6.1.3 0 .7-.2 1l-2.3 2.2z"/></svg>
        <span>+31 647315082</span>
      </li>
      <li>
        <svg viewBox="0 0 24 24" aria-hidden="true" fill="none" stroke="var(--pink)" stroke-width="1.8"><circle cx="12" cy="12" r="9"/><ellipse cx="12" cy="12" rx="4" ry="9"/><path d="M3 12h18M4.5 7.5h15M4.5 16.5h15"/></svg>
        <span>www.poppelhoek.nl</span>
      </li>
    </ul>
    <div class="address-band">Kastanjeweg 47 B, 2316 KR Leiden</div>
  </section>
</main>
</body>
</html>
```